Life insurance company website and landing page

Web design is required for life insurance company. Specifically the company will 1) generate leads and 2) provide a blog. The target market of this business is people in their 50s and 60s, medium-high to high income earners, who are likely to have a policy in place already but want to save money on their premiums. Please read the attached design brief for more guidance. Open to any concepts that might work.The outputs for this job will include:1) a website2) a landing page3) fixing logos into a more useful and professional format (this should take 5 mins with the correct software)
Colors
Designer to choose colors to be used in the design.
Look and feel
Each slider illustrates characteristics of the customer's brand and the style your logo design should communicate.

```html
<!DOCTYPE html>
<html lang="en">
<head>
<meta charset="utf-8">
<title>CoverCompare.Life – Compare Life Insurers</title>
<link rel="stylesheet" href="https://fonts.googleapis.com/css2?family=Fira+Sans:ital,wght@0,400;0,500;0,600;0,700;0,800;1,500&family=Source+Sans+3:wght@400;600;700&display=swap">
<style>
:root{
  --orange:#f5a21b;
  --gold:#f2c14e;
  --red:#e8413c;
  --green:#6cbf00;
  --grey:#7a7a7a;
  --ink:#222;
  --muted:#808080;
  --topbar:#2b2b2b;
  --footer:#1f1f1f;
  --bottom:#0f0f1c;
  --soft:#f1f1f1;
}
*{box-sizing:border-box;margin:0;padding:0}
html,body{width:1200px;height:3788px;overflow:hidden}
body{position:relative;background:#fff;font-family:"Source Sans 3",sans-serif;color:var(--ink)}
.abs{position:absolute}
.topbar{left:0;top:0;width:1200px;height:44px;background:var(--topbar)}
.topbar .social{left:50px;top:12px;display:flex;gap:6px}
.topbar .social span{width:19px;height:19px;border:2px solid #fff;border-radius:50%;display:block}
.topbar .account{right:26px;top:0;height:44px;display:flex;align-items:center;gap:26px;color:#fff;font-family:"Fira Sans",sans-serif;font-weight:600;font-size:15px}
.topbar .account span{display:flex;align-items:center;gap:7px}
.header{left:0;top:44px;width:1200px;height:84px;background:#fff;box-shadow:0 2px 6px rgba(0,0,0,.04)}
.brand{display:flex;align-items:center;gap:12px;font-family:"Fira Sans",sans-serif;font-weight:500;font-size:28px;color:var(--ink)}
.brand .mark{width:36px;height:36px;border:4px solid var(--red);border-radius:6px}
.header .brand{left:50px;top:22px}
.nav{left:637px;top:32px;display:flex;gap:55px;font-family:"Fira Sans",sans-serif;font-weight:600;font-size:14px;letter-spacing:.3px}
.nav .active{color:var(--red)}
.btn{border:2px solid var(--gold);border-radius:22px;background:#fff;font-family:"Fira Sans",sans-serif;font-weight:500;display:flex;align-items:center;justify-content:center;box-shadow:0 3px 8px rgba(242,193,78,.35)}
.header .btn{left:997px;top:22px;width:152px;height:38px;font-size:14px;font-weight:600;gap:6px}
.hero{left:0;top:128px;width:1200px;height:507px;background:#fafafa}
.hero h1{left:50px;top:115px;font-family:"Fira Sans",sans-serif;font-weight:800;font-size:40px;line-height:56px;color:#111;text-shadow:2px 2px 0 var(--gold)}
.hero .lede{left:50px;top:245px;font-family:"Fira Sans",sans-serif;font-style:italic;font-weight:500;font-size:23px;color:#333}
.hero .btn{left:50px;top:323px;width:252px;height:56px;font-size:20px}
.hero-art{left:690px;top:34px;width:465px;height:473px;background:radial-gradient(circle at 55% 65%,#e53935 0 18%,#2e9e5b 19% 30%,transparent 31%),radial-gradient(circle at 50% 40%,#ffd36b 0 30%,#fff1cc 55%,transparent 70%)}
.chart-sec{left:0;top:635px;width:1200px;height:627px;background:#fff}
.chart-card{left:48px;top:55px;width:1102px;height:517px;background:#fff;box-shadow:0 2px 14px rgba(0,0,0,.12)}
.chart-svg{left:0;top:0;width:1102px;height:517px}
.info-card{left:625px;top:50px;width:423px;height:385px;background:#fff;box-shadow:0 2px 12px rgba(0,0,0,.12);padding:45px 46px}
.info-card h2{font-family:"Fira Sans",sans-serif;font-weight:500;font-size:25px;line-height:36px;color:#333}
.info-card p{margin-top:16px;font-size:15px;line-height:31px;color:var(--muted)}
.info-card .btn{position:absolute;left:131px;top:295px;width:160px;height:38px;font-size:14px}
.sec-title{display:flex;align-items:center;gap:20px;font-family:"Fira Sans",sans-serif;font-weight:700;font-size:24px;color:#333;letter-spacing:.3px}
.sec-title .mark{width:34px;height:40px;border:3px solid #333;border-radius:5px}
.benefits{left:0;top:1262px;width:1200px;height:608px;background:var(--soft)}
.benefits .sec-title{left:478px;top:56px}
.benefit{top:164px;width:357px;height:392px;background:#fff;border-radius:18px;box-shadow:0 2px 10px rgba(0,0,0,.06);text-align:center;padding-top:50px}
.benefit .icon{width:144px;height:144px;border-radius:50%;margin:0 auto;box-shadow:0 3px 14px rgba(0,0,0,.16);display:flex;align-items:center;justify-content:center}
.benefit h3{margin:20px auto 0;width:290px;font-family:"Fira Sans",sans-serif;font-weight:500;font-size:20px;line-height:30px;color:var(--orange)}
.benefit p{margin:14px auto 0;width:300px;font-size:15px;line-height:24px;color:var(--muted)}
.benefit.left p{text-align:left}
.insurers{left:0;top:1870px;width:1200px;height:303px;background:#fafafa}
.insurers .sec-title{left:482px;top:58px}
.logo-tile{top:155px;width:235px;height:93px;background:#fff;display:flex;align-items:center;justify-content:center;font-family:"Fira Sans",sans-serif;font-weight:700;font-size:32px}
.arrow{width:20px;height:30px}
.testi{left:0;top:2173px;width:1200px;height:658px;background:#fff}
.testi .sec-title{left:412px;top:55px}
.testi .intro{left:300px;top:130px;width:600px;text-align:center;font-size:15px;line-height:24px;color:var(--muted)}
.quote-mark{font-family:"Fira Sans",sans-serif;font-weight:800;font-size:110px;color:var(--orange);line-height:1}
.t-card{top:228px;width:443px;height:300px;background:#fff;box-shadow:0 2px 14px rgba(0,0,0,.12);text-align:center;padding-top:38px}
.t-card p{margin:18px auto 0;width:270px;font-size:11.5px;line-height:19px;color:var(--muted)}
.t-card .rule{width:44px;height:2px;background:var(--orange);margin:16px auto 0}
.t-card h4{margin-top:18px;font-family:"Fira Sans",sans-serif;font-weight:600;font-size:15px;color:#222}
.dots{left:559px;top:597px;display:flex;gap:10px;align-items:center}
.dots span{width:7px;height:7px;border-radius:50%;background:#ccc}
.dots .on{width:9px;height:9px;background:var(--orange)}
.contact{left:0;top:2831px;width:1200px;height:523px;background:#fff}
.contact-box{left:48px;top:48px;width:1103px;height:422px;background:linear-gradient(90deg,#fff 0,#fff 85%,#fff7e3 100%);box-shadow:inset 0 0 28px rgba(242,193,78,.35)}
.contact-photo{left:0;top:0;width:545px;height:422px;background:linear-gradient(135deg,#8d9099 0%,#4a5a78 45%,#1f3566 75%,#152447 100%);clip-path:polygon(0 0,100% 0,51% 100%,0 100%)}
.contact .sec-title{left:717px;top:104px}
.field{width:222px;height:38px;border:1.5px solid #ddd;background:#fff;display:flex;align-items:center;gap:8px;padding-left:10px;font-size:14px;color:#999}
.contact .btn{left:768px;top:387px;width:117px;height:36px;font-size:14px}
.footer{left:0;top:3354px;width:1200px;height:344px;background:var(--footer);color:#fff}
.footer .brand{left:48px;top:60px;color:#fff;font-size:24px;font-weight:600}
.footer .brand .mark{border-color:#fff;width:46px;height:50px}
.footer .about{left:50px;top:146px;width:300px;font-size:14px;line-height:26px;color:#ddd}
.footer h5{font-family:"Fira Sans",sans-serif;font-weight:600;font-size:19px}
.footer ul{list-style:none;font-size:14px;line-height:39px;color:#eee;margin-top:14px}
.footer .col{top:51px}
.contact-list{font-size:14px;color:#eee}
.contact-list div{display:flex;gap:16px;align-items:flex-start;margin-top:16px;line-height:31px}
.footer .socials{left:926px;top:272px;display:flex;gap:22px}
.footer .socials span{width:30px;height:30px;border:2px solid #fff;border-radius:50%;display:block}
.bottom{left:0;top:3698px;width:1200px;height:90px;background:var(--bottom);color:#fff;font-size:14px}
.bottom .links{left:48px;top:34px;display:flex;gap:7px}
.bottom .copy{right:49px;top:34px}
</style>
</head>
<body>

<div class="abs topbar">
  <div class="abs social"><span></span><span></span><span></span><span></span></div>
  <div class="abs account">
    <span><svg width="16" height="14" viewBox="0 0 16 14"><rect x="1" y="2" width="11" height="11" fill="none" stroke="#fff" stroke-width="1.6"/><path d="M6 9l8-8" stroke="#fff" stroke-width="2"/></svg>Register</span>
    <span><svg width="16" height="16" viewBox="0 0 16 16"><circle cx="8" cy="5" r="4" fill="#fff"/><path d="M1 16c0-5 3-6 7-6s7 1 7 6z" fill="#fff"/></svg>Login</span>
    <span><svg width="18" height="18" viewBox="0 0 18 18"><circle cx="7.5" cy="7.5" r="5.5" fill="none" stroke="#fff" stroke-width="2"/><path d="M11.5 11.5l5 5" stroke="#fff" stroke-width="2"/></svg></span>
  </div>
</div>

<header class="abs header">
  <div class="abs brand"><span class="mark"></span>CoverCompare.Life</div>
  <nav class="abs nav"><span class="active">HOME</span><span>CONTACT US</span><span>BLOG</span></nav>
  <div class="abs btn"><svg width="14" height="14" viewBox="0 0 24 24"><path d="M6.6 10.8a15 15 0 0 0 6.6 6.6l2.2-2.2c.3-.3.7-.4 1-.2 1.1.4 2.3.6 3.6.6.6 0 1 .4 1 1V20c0 .6-.4 1-1 1A17 17 0 0 1 3 4c0-.6.4-1 1-1h3.5c.6 0 1 .4 1 1 0 1.3.2 2.5.6 3.6.1.3 0 .7-.2 1z" fill="var(--orange)"/></svg>CONTACT US</div>
</header>

<section class="abs hero">
  <h1 class="abs">COMPARE AUSTRALIA'S LEADING<br>LIFE INSURERS FREE TODAY</h1>
  <p class="abs lede">“Make sure your insurer isn't charging you too much”</p>
  <div class="abs btn">Compare quotes now</div>
  <div class="abs hero-art" role="img" aria-label="Illustration of a family surrounded by colourful insurance icons for health, home, car and savings"></div>
</section>

<section class="abs chart-sec">
  <div class="abs chart-card">
    <svg class="abs chart-svg" viewBox="0 0 750 352" font-family="Source Sans 3, sans-serif" font-size="9.5" fill="#333">
      <line x1="92" y1="37" x2="92" y2="264" stroke="#dcdcf0" stroke-width="3"/>
      <line x1="92" y1="264" x2="369" y2="264" stroke="#dcdcf0" stroke-width="3"/>
      <g stroke="#999" stroke-width="1">
        <line x1="86" y1="118" x2="92" y2="118"/><line x1="86" y1="151" x2="92" y2="151"/><line x1="86" y1="172" x2="92" y2="172"/><line x1="86" y1="184" x2="92" y2="184"/><line x1="86" y1="203" x2="92" y2="203"/><line x1="86" y1="217" x2="92" y2="217"/><line x1="86" y1="226" x2="92" y2="226"/>
      </g>
      <g text-anchor="end" dominant-baseline="middle">
        <text x="83" y="118">$1007</text><text x="83" y="151">$987</text><text x="83" y="172">$844</text><text x="83" y="184">$750</text><text x="83" y="203">$630</text><text x="83" y="217">$528</text><text x="83" y="226">$460</text>
      </g>
      <text x="81" y="277" text-anchor="middle" font-size="11">0</text>
      <rect x="100" y="224" width="31" height="33" fill="#f0493e"/>
      <rect x="137" y="218" width="31" height="39" fill="var(--grey)"/>
      <rect x="174" y="203" width="31" height="54" fill="var(--green)"/>
      <rect x="211" y="185" width="31" height="72" fill="#cfcfcf"/>
      <rect x="248" y="172" width="31" height="85" fill="#f0493e"/>
      <rect x="285" y="151" width="31" height="106" fill="var(--green)"/>
      <rect x="322" y="120" width="31" height="137" fill="var(--grey)"/>
      <g font-size="8.5">
        <text transform="translate(113 214) rotate(-90)">Cover</text><text transform="translate(122 214) rotate(-90)">Compare.life</text>
        <text transform="translate(150 208) rotate(-90)">Loreum</text><text transform="translate(159 208) rotate(-90)">ipsum</text>
        <text transform="translate(187 193) rotate(-90)">Loreum</text><text transform="translate(196 193) rotate(-90)">ipsum</text>
        <text transform="translate(224 175) rotate(-90)">Loreum</text><text transform="translate(233 175) rotate(-90)">ipsum</text>
        <text transform="translate(261 162) rotate(-90)">Loreum</text><text transform="translate(270 162) rotate(-90)">ipsum</text>
        <text transform="translate(298 141) rotate(-90)">Loreum</text><text transform="translate(307 141) rotate(-90)">ipsum</text>
        <text transform="translate(335 110) rotate(-90)">Loreum</text><text transform="translate(344 110) rotate(-90)">ipsum</text>
      </g>
      <g text-anchor="middle">
        <text x="110" y="291">$460</text><text x="147" y="291">$528</text><text x="184" y="291">$630</text><text x="221" y="291">$750</text><text x="258" y="291">$844</text><text x="295" y="291">$987</text><text x="334" y="291">$1007</text>
      </g>
      <text x="211" y="316" text-anchor="middle" font-size="12">x-axis</text>
      <path d="M235 312h22M252 309l5 3-5 3" stroke="#999" fill="none"/>
      <text transform="translate(44 180) rotate(-90)" text-anchor="middle" font-size="12">y-axis</text>
      <path d="M40 152v-18M37 139l3-5 3 5" stroke="#999" fill="none"/>
    </svg>
    <div class="abs info-card">
      <h2>Bar chart to illustrate the difference in price .</h2>
      <p>Lorem Ipsum is simply dummy text of the printing and typesetting industry. Lorem Ipsum has been the industry's standard dummy text ever since the 1500s.</p>
      <div class="btn">Get a quote</div>
    </div>
  </div>
</section>

<section class="abs benefits">
  <div class="abs sec-title"><span class="mark"></span>3 KEY BENEFITS</div>
  <article class="abs benefit left" style="left:51px">
    <div class="icon"><svg width="90" height="90" viewBox="0 0 90 90" fill="none" stroke="#222" stroke-width="3"><circle cx="45" cy="32" r="20"/><circle cx="45" cy="32" r="8"/><path d="M8 62l22-10 15 8 15-8 22 10M20 70l16 10M70 70l-16 10"/></svg></div>
    <h3>We only work with Australia's most trusted brands</h3>
    <p>You can be confident in that your insurer will be there for you, and your family, when you need them the most</p>
  </article>
  <article class="abs benefit" style="left:422px">
    <div class="icon"><svg width="90" height="96" viewBox="0 0 90 96" fill="none" stroke="#222" stroke-width="5"><path d="M45 6c12 8 24 10 36 10v30c0 24-16 38-36 44C25 84 9 70 9 46V16c12 0 24-2 36-10z"/><circle cx="45" cy="48" r="20"/><path d="M35 48l7 7 13-14"/></svg></div>
    <h3>Price beat<br>Guarantee</h3>
    <p>We guarantee to beat any quote for a comparable &nbsp;level of cover must be a stepped premium.</p>
  </article>
  <article class="abs benefit" style="left:794px">
    <div class="icon"><svg width="90" height="90" viewBox="0 0 90 90" fill="none" stroke="#222" stroke-width="3.5"><circle cx="45" cy="45" r="38"/><circle cx="52" cy="34" r="11" fill="#222"/><text x="52" y="39" font-size="14" fill="#fff" stroke="none" text-anchor="middle" font-family="Fira Sans, sans-serif" font-weight="700">$</text><path d="M14 55c10-6 18-6 26 0h12c4 0 4 6 0 6H38M22 68c14 4 30 2 44-10"/></svg></div>
    <h3>No hidden<br>fees</h3>
    <p>Simple pricing that is easy to understand.<br>No hidden fees or charges</p>
  </article>
</section>

<section class="abs insurers">
  <div class="abs sec-title"><span class="mark"></span>OUR INSURERS</div>
  <svg class="abs arrow" style="left:48px;top:188px" viewBox="0 0 20 30"><path d="M14 5L5 15l9 10" fill="none" stroke="#555" stroke-width="2.5"/></svg>
  <div class="abs logo-tile" style="left:94px;color:#5cb531">Kora Life</div>
  <div class="abs logo-tile" style="left:353px;color:#f2a21b">Meridian</div>
  <div class="abs logo-tile" style="left:610px;color:#3f8a52">Northway</div>
  <div class="abs logo-tile" style="left:868px;color:#1b3a8f">Halden</div>
  <svg class="abs arrow" style="left:1133px;top:188px" viewBox="0 0 20 30"><path d="M6 5l9 10-9 10" fill="none" stroke="#555" stroke-width="2.5"/></svg>
</section>

<section class="abs testi">
  <div class="abs sec-title"><span class="mark"></span>CUSTOMER TESTIMONIAL</div>
  <p class="abs intro">Lorem Ipsum is simply dummy text of the printing and typesetting industry. Lorem Ipsum has been the industry's standard dummy text ever since the 1500s,</p>
  <svg class="abs arrow" style="left:48px;top:332px" viewBox="0 0 20 30"><path d="M14 5L5 15l9 10" fill="none" stroke="#555" stroke-width="2.5"/></svg>
  <div class="abs quote-mark" style="left:108px;top:200px">“</div>
  <article class="abs t-card" style="left:118px">
    <svg width="44" height="48" viewBox="0 0 44 48"><circle cx="22" cy="14" r="12" fill="var(--orange)"/><path d="M2 48c0-14 9-20 20-20s20 6 20 20z" fill="var(--orange)"/></svg>
    <p>Lorem Ipsum is simply dummy text of the printing and typesetting industry.Lorem Ipsum has been the &nbsp;industry's standard dummy text ever since</p>
    <div class="rule"></div>
    <h4>Daniel Hart</h4>
  </article>
  <article class="abs t-card" style="left:637px">
    <svg width="44" height="48" viewBox="0 0 44 48"><circle cx="22" cy="14" r="12" fill="var(--orange)"/><path d="M2 48c0-14 9-20 20-20s20 6 20 20z" fill="var(--orange)"/></svg>
    <p>Lorem Ipsum is simply dummy text of the printing and typesetting industry.Lorem Ipsum has been the &nbsp;industry's standard dummy text ever since</p>
    <div class="rule"></div>
    <h4>Daniel Hart</h4>
  </article>
  <div class="abs quote-mark" style="left:1025px;top:200px">”</div>
  <svg class="abs arrow" style="left:1133px;top:332px" viewBox="0 0 20 30"><path d="M6 5l9 10-9 10" fill="none" stroke="#555" stroke-width="2.5"/></svg>
  <div class="abs dots"><span></span><span class="on"></span><span></span><span></span><span></span></div>
</section>

<section class="abs contact">
  <div class="abs contact-box">
    <div class="abs contact-photo" role="img" aria-label="Photo of a businessman in a suit holding a smartphone"></div>
  </div>
  <div class="abs sec-title"><span class="mark"></span>CONTACT US</div>
  <div class="abs field" style="left:578px;top:204px"><svg width="14" height="14" viewBox="0 0 16 16"><circle cx="8" cy="5" r="4" fill="var(--orange)"/><path d="M1 16c0-5 3-6 7-6s7 1 7 6z" fill="var(--orange)"/></svg>First Name</div>
  <div class="abs field" style="left:853px;top:204px"><svg width="14" height="14" viewBox="0 0 16 16"><circle cx="8" cy="5" r="4" fill="var(--orange)"/><path d="M1 16c0-5 3-6 7-6s7 1 7 6z" fill="var(--orange)"/></svg>Last Name</div>
  <div class="abs field" style="left:578px;top:262px"><svg width="16" height="16" viewBox="0 0 24 24"><path d="M6.6 10.8a15 15 0 0 0 6.6 6.6l2.2-2.2c.3-.3.7-.4 1-.2 1.1.4 2.3.6 3.6.6.6 0 1 .4 1 1V20c0 .6-.4 1-1 1A17 17 0 0 1 3 4c0-.6.4-1 1-1h3.5c.6 0 1 .4 1 1 0 1.3.2 2.5.6 3.6.1.3 0 .7-.2 1z" fill="var(--orange)"/></svg>Phone Number</div>
  <div class="abs field" style="left:853px;top:262px"><svg width="16" height="12" viewBox="0 0 16 12"><rect width="16" height="12" fill="var(--orange)"/><path d="M0 0l8 6 8-6" fill="none" stroke="#fff" stroke-width="1.5"/></svg>Email</div>
  <div class="abs field" style="left:578px;top:319px"><svg width="16" height="16" viewBox="0 0 16 16"><rect x="1" y="3" width="14" height="12" fill="none" stroke="var(--orange)" stroke-width="1.6"/><rect x="1" y="3" width="14" height="3" fill="var(--orange)"/><rect x="6" y="9" width="4" height="3" fill="var(--orange)"/></svg>Age</div>
  <div class="abs field" style="left:853px;top:319px"><svg width="14" height="16" viewBox="0 0 14 16"><circle cx="7" cy="10" r="6" fill="var(--orange)"/><path d="M4 1h6L8 4H6z" fill="var(--orange)"/></svg>Cover Amount</div>
  <div class="abs btn">Submit</div>
</section>

<footer class="abs footer">
  <div class="abs brand"><span class="mark"></span>CoverCompare.life</div>
  <p class="abs about">This is Photoshop's version &nbsp;of Lorem Ipsum. Proin gravida nibh vel velit auctor aliquet. Aenean sollicitudin, lorem quis bibendum auctor, nisi elit consequat ipsum, nec sagittis</p>
  <div class="abs col" style="left:437px"><h5>Company</h5><ul><li>About our company</li><li>Get a quote</li><li>Blog</li><li>Contact us</li><li>Work With Us</li></ul></div>
  <div class="abs col" style="left:716px"><h5>Blog</h5><ul><li>HealthCare</li><li>Automation</li><li>Construction</li><li>Car Insurace</li></ul></div>
  <div class="abs col" style="left:925px"><h5>Contact Us</h5>
    <div class="contact-list">
      <div><svg width="16" height="22" viewBox="0 0 16 22"><path d="M8 0a8 8 0 0 0-8 8c0 6 8 14 8 14s8-8 8-14a8 8 0 0 0-8-8z" fill="#fff"/><circle cx="8" cy="8" r="3" fill="var(--footer)"/></svg><span>#42 Harbour Lane, Level 3<br>Eastfield, AU</span></div>
      <div><svg width="22" height="22" viewBox="0 0 24 24"><path d="M6.6 10.8a15 15 0 0 0 6.6 6.6l2.2-2.2c.3-.3.7-.4 1-.2 1.1.4 2.3.6 3.6.6.6 0 1 .4 1 1V20c0 .6-.4 1-1 1A17 17 0 0 1 3 4c0-.6.4-1 1-1h3.5c.6 0 1 .4 1 1 0 1.3.2 2.5.6 3.6.1.3 0 .7-.2 1z" fill="#fff"/></svg><span>+61-555-0142</span></div>
      <div><svg width="24" height="18" viewBox="0 0 24 18"><rect x="1" y="1" width="22" height="16" fill="none" stroke="#fff" stroke-width="1.6"/><path d="M1 1l11 9 11-9" fill="none" stroke="#fff" stroke-width="1.6"/></svg><span>hello@covercompare.example</span></div>
    </div>
  </div>
  <div class="abs socials"><span></span><span></span><span></span><span></span></div>
</footer>

<div class="abs bottom">
  <div class="abs links"><span>Contact Us</span><span>Terms of Use</span><span>Privacy Policy</span><span>Cookie Policy</span><span>Site Map</span></div>
  <div class="abs copy">Copyright 2019 CoverCompare.life All Rights Reserved.</div>
</div>

</body>
</html>
```